IT Services Business Card Design

We require a business card design for an IT services company called RT Code Transit.

We specialize in taking an organisations software and readying it for deployment to new environments (e.g. Nex 3 to Nex 5). This process is termed application packaging. This is not the same as putting things in boxes but I am happy to use boxes as a pun icon ;-) This is our second step in branding, we currently have a new logo and our poor excuse of a website is next to be updated but it contains information on who we are and what we cover at rtcodetransit.example

We are looking for a fun, modern but stylish and professional looking design.

I have attached the logo in multiple formats including vector formats (and the fonts that created the logo if required)
Updates

Thanks to all the designers so far, some great designs in there.  I will be selecting a card design on the deadline date. 

However, there is still time to submit some more designs.  The majority of the ones I have so far are typical simplistic designs that we have all seen before and I have enough of those to choose from now.  If you wish to submit any more designs, please submit somthing unusual to grab our attention.

Target Market(s)

Project executives of large organisations looking for Nexora migrations

Industry/Entity Type

Software

Requirements
Must have
• Want to show company name, contact name, title, main number, contact number, fax number, email address and website address. I do not want to show the address.
Must use the attached logo, retaining the colours in them.

This has to be a double-sided design. I will be using pelby.example and will be selecting their rounded corner business card design.

Their templates and design requirements (sizing etc.) can be found here: http://uk.pelby.example/help/faq/templates-and-guidelines.html

Happy for company name or website to be on either side of the card.

This design has to be original and not used before for another company

Would like to style it around the business colours in the logo
Nice to have
• Pelby.example has an option for multiple card designs to appear on the back. If this is possible in the budget and time you have and you have a design(s) that work with that but carry the same style and theme, that would be nice to see but not necessary.
Should not have
• We do not want to put a postal address on the cards

```html
<!DOCTYPE html>
<html lang="en">
<head>
<meta charset="utf-8">
<title>RT Code Transit – Business Card</title>
<link rel="stylesheet" href="https://fonts.googleapis.com/css2?family=Jost:wght@300;400&family=Arimo:wght@400;700&family=Libre+Baskerville:wght@700&display=swap">
<style>
  :root {
    --paper: #ffffff;
    --ink: #111111;
    --brand-grey: #6b625a;
    --brand-blue: #4a74d9;
    --dark-card: #272d28;
    --light-text: #e4e4e4;
    --line-grey: #9a9a9a;
  }
  * { margin: 0; padding: 0; box-sizing: border-box; }
  html, body { width: 1200px; height: 1043px; overflow: hidden; background: var(--paper); }
  .sheet { position: relative; width: 1200px; height: 1043px; font-family: "Jost", sans-serif; color: var(--ink); }

  .side-title { position: absolute; left: 105px; font-family: "Jost", sans-serif; font-weight: 300; font-size: 64px; letter-spacing: 4px; line-height: 1; }
  .side-title--front { top: 24px; }
  .side-title--back { top: 588px; }
  .spec { position: absolute; left: 107px; top: 94px; font-size: 16px; line-height: 22px; }

  .card { position: absolute; width: 504px; height: 310px; overflow: hidden; }
  .card--front-light { left: 82px; top: 152px; background: var(--paper); border: 1px solid #555; }
  .card--front-dark { left: 599px; top: 152px; background: var(--dark-card); }
  .card--back-1 { left: 75px; top: 667px; border: 1px solid #888; background: var(--paper); }
  .card--back-2 { left: 621px; top: 667px; border: 2px solid var(--ink); background: var(--paper); }

  .brand { position: absolute; display: flex; align-items: center; white-space: nowrap; font-family: "Jost", sans-serif; font-weight: 400; color: var(--brand-grey); }
  .brand__dot { border-radius: 50%; background: var(--brand-blue); flex: none; }
  .brand--large { left: 52px; top: 108px; font-size: 42px; gap: 18px; }
  .brand--large .brand__dot { width: 74px; height: 74px; }
  .card--front-dark .brand { color: var(--light-text); }
  .brand--small { font-size: 21px; gap: 10px; }
  .brand--small .brand__dot { width: 40px; height: 40px; }
  .card--back-1 .brand--small { left: 262px; top: 30px; }
  .card--back-2 .brand--small { left: 258px; top: 34px; }

  .website { position: absolute; left: 237px; top: 218px; font-family: "Arimo", sans-serif; font-size: 15px; color: var(--brand-grey); }
  .card--front-dark .website { color: var(--light-text); left: 240px; top: 228px; }

  .person { position: absolute; color: var(--brand-grey); }
  .person__name { font-family: "Libre Baskerville", serif; font-weight: 700; font-size: 19px; letter-spacing: 1px; color: var(--ink); }
  .person__name small { font-size: 13px; margin-left: 6px; }
  .person__title { font-family: "Arimo", sans-serif; font-size: 12px; color: var(--ink); margin-top: 2px; }
  .card--back-1 .person { left: 48px; top: 76px; }
  .card--back-2 .person { left: 32px; top: 46px; }
  .card--back-2 .person__name { color: var(--brand-grey); }
  .card--back-2 .person__title { color: var(--brand-grey); }

  .contact { position: absolute; font-family: "Arimo", sans-serif; color: var(--brand-grey); }
  .card--back-1 .contact { left: 222px; top: 222px; font-size: 13.5px; line-height: 17px; }
  .card--back-2 .contact { left: 0; width: 100%; top: 226px; text-align: center; font-size: 11px; line-height: 15px; }
  .contact__main { font-weight: 700; font-size: 16px; line-height: 24px; }

  .icons { position: absolute; left: 0; top: 0; }
  .label { position: absolute; top: 990px; font-family: "Arimo", sans-serif; font-size: 25px; letter-spacing: 1px; }
  .label--1 { left: 83px; }
  .label--2 { left: 626px; }
</style>
</head>
<body>
<div class="sheet">
  <h1 class="side-title side-title--front">FRONT</h1>
  <p class="spec">Namecard<br>Size : 8.8 cm x 5.4 cm</p>

  <section class="card card--front-light">
    <div class="brand brand--large"><span>RT Code Transit</span><span class="brand__dot"></span></div>
    <p class="website">rtcodetransit.example</p>
  </section>

  <section class="card card--front-dark">
    <div class="brand brand--large"><span>RT Code Transit</span><span class="brand__dot"></span></div>
    <p class="website">rtcodetransit.example</p>
  </section>

  <h2 class="side-title side-title--back">BACK</h2>

  <section class="card card--back-1">
    <div class="brand brand--small"><span>RT Code Transit</span><span class="brand__dot"></span></div>
    <div class="person">
      <p class="person__name">MILES<small>OAKEN</small></p>
      <p class="person__title">ENGINEERING</p>
    </div>
    <svg class="icons" width="504" height="310" viewBox="0 0 504 310" aria-hidden="true">
      <polyline points="40,112 28,112 28,152 48,152" fill="none" stroke="var(--line-grey)" stroke-width="1"/>
      <!-- monitor: user -->
      <rect x="50" y="138" width="84" height="58" fill="none" stroke="var(--ink)" stroke-width="5"/>
      <rect x="82" y="198" width="20" height="10" fill="var(--ink)"/>
      <rect x="68" y="208" width="48" height="5" fill="var(--ink)"/>
      <rect x="78" y="160" width="28" height="30" fill="var(--ink)"/>
      <!-- monitor: chart -->
      <rect x="212" y="138" width="84" height="58" fill="none" stroke="var(--brand-grey)" stroke-width="5"/>
      <rect x="244" y="198" width="20" height="10" fill="var(--brand-grey)"/>
      <rect x="230" y="208" width="48" height="5" fill="var(--brand-grey)"/>
      <polyline points="220,180 232,180 240,160 248,178 258,150 266,172 274,158 288,158" fill="none" stroke="var(--brand-grey)" stroke-width="2"/>
      <!-- monitor: upload -->
      <rect x="370" y="138" width="84" height="58" fill="none" stroke="var(--brand-blue)" stroke-width="5"/>
      <rect x="402" y="198" width="20" height="10" fill="var(--brand-blue)"/>
      <rect x="388" y="208" width="48" height="5" fill="var(--brand-blue)"/>
      <polygon points="412,148 438,168 426,168 426,188 398,188 398,168 386,168" fill="var(--brand-blue)"/>
      <polyline points="470,150 470,137 454,137" fill="none" stroke="var(--brand-blue)" stroke-width="1"/>
      <polyline points="198,222 198,230 214,230" fill="none" stroke="var(--line-grey)" stroke-width="1"/>
    </svg>
    <div class="contact">
      <p>M &nbsp;&nbsp;: 011 44 20 7000 0101</p>
      <p>DID: 011 44 20 7000 0202</p>
      <p>FAX: 011 44 20 7000 0303</p>
      <p>milesoaken@rtcodetransit.example</p>
    </div>
  </section>

  <section class="card card--back-2">
    <div class="person">
      <p class="person__name">MILES<small>OAKEN</small></p>
      <p class="person__title">ENGINEERING</p>
    </div>
    <div class="brand brand--small"><span>RT Code Transit</span><span class="brand__dot"></span></div>
    <svg class="icons" width="504" height="310" viewBox="0 0 504 310" aria-hidden="true">
      <defs>
        <marker id="arrowhead" markerWidth="8" markerHeight="8" refX="6" refY="4" orient="auto">
          <path d="M0,0 L8,4 L0,8 Z" fill="var(--ink)"/>
        </marker>
      </defs>
      <g fill="none" stroke="var(--ink)" stroke-width="4">
        <rect x="156" y="101" width="62" height="40"/>
        <rect x="280" y="101" width="62" height="40"/>
        <rect x="220" y="159" width="60" height="38"/>
      </g>
      <g fill="var(--ink)">
        <rect x="178" y="143" width="18" height="6"/><rect x="168" y="149" width="38" height="4"/>
        <rect x="302" y="143" width="18" height="6"/><rect x="292" y="149" width="38" height="4"/>
        <rect x="241" y="199" width="18" height="6"/><rect x="231" y="205" width="38" height="4"/>
      </g>
      <g fill="none" stroke="var(--ink)" stroke-width="2" marker-end="url(#arrowhead)">
        <path d="M270,108 Q250,96 230,108"/>
        <path d="M180,160 Q186,180 210,186"/>
        <path d="M290,184 Q312,176 314,156"/>
      </g>
    </svg>
    <div class="contact">
      <p class="contact__main">M: 011 44 20 7000 0101</p>
      <p>DID: 011 44 20 7000 0202 &nbsp;&nbsp;&nbsp; FAX: 011 44 20 7000 0303</p>
      <p>milesoaken@rtcodetransit.example</p>
    </div>
  </section>

  <p class="label label--1">option 1</p>
  <p class="label label--2">option 2</p>
</div>
</body>
</html>
```